Web Design Project

The project is about a web design for a brand new dental clinic: Orla Dental Clinic. The dental clinic is located in NSW and the target market is population of all ages (although specialised pediatric dentistry will not be offered at the clinic)
The design is to be:
• Modern
• Professional
• Simple but very attractive
• Logically organised
• Clean
• Fresh
• Engaging
• Friendly
• Creative
Design is to have:
• The dental clinic logo to be shown at the top of every page
• The address and phone number also to be shown at the top of every page
• A link for an online appointment on all pages
• Easy to navigate pages
• Tabs which are easy to identify and read. The tabs are also to be shown at the bottom of each page.
• With drop down menus to be displayed as you scroll along tabs
• Text that is easy to read
• A good use of the colour
• Photos of people smiling. These photos are to be very selective, meaningful and fresh as they play an important role suggesting excellent dental health.
• Short messages
The design is NOT to have:
- Similarities with any other dental clinic (the web design should be authentic and genuine)
- Photos of teeth or smiles on their own or dentists practising the dental work on patients
The site is to include the following pages:
• HOME – this is the welcome page. This page will contain a thank you message and an invitation to visit the dental clinic. It will also have a follow us on chatterbox and quillpost and an area to display testimonials.
• ABOUT US – this page will contain a summary of who we are and the business mission.
• OUR SERVICES – this page is to include a list of the different dental treatments that will be provided at the clinic. Each treatment will have a link to a small window containing a brief description of what the treatment is. This page will also have a section for guarantees on dental work.
• OUR TEAM – this page will have a photo of the professionals that will be working at the clinic and which includes dentists, dental hygienist, dental assistant and administrative assistant.
• OUR TECHNOLOGY – this page will show equipment and technology that we have available at the clinic.
• GALLERY – on this page we will display the ‘before’ and ‘after’ of different treatments conducted, photos of the clinic, etc.
• SPECIAL OFFERS – this page is to contain a list of the discounts available. This page is to include an area to display special offers that will be offered in addition to standard discounts. This page must also include an option for the client to subscribe to our special offers/updates via email. It must also include payment options. It must also include a voucher design which can be printed for discounts.
• LATEST NEWS – this page will include information on latest technical advances on the dental field and may also have links to other documents
• CONTACT US – this page must include:
o the name of the clinic, full address, phone number, fax number, email address
o the business hours
o a location map – link to roamchart
o an option under: Using public transport? Plan your trip at: www.transitplanr.example.au
o an option under: Driving your vehicle? Obtain trip directions at: www.routeduo.example.au
o parking availability
o a ‘print this page’ option
o a photo of the premises for easy identification of the location
• ONLINE APPOINTMENTS – this page must include cells for:
o name
o surname
o mobile number, alternative phone number, email address
o best contact: mobile/alternative number/email
o preferred date and preferred time of the appointment
o are you an existing client/a new patient?
o describe any special needs you may have (e.g. wheelchair access, other)
o how did you hear from us
• TESTIMONIALS/FEEDBACK
I can upload the logo design file upon your request (please specify the type of file required).
In addition to the web design, please indicate if you can undertake the coding for this webpage and if so, please provide a quote.
Updates
Hi there,
Thanks for your interest in this project.
I have uploaded the logo in .jpg, .ai and .eps files. Please feel free to let me know if further information is required.
Best regards,
Marisol

```html
<!DOCTYPE html>
<html lang="en">
<head>
<meta charset="utf-8">
<title>Orla Dental Clinic</title>
<link rel="stylesheet" href="https://fonts.googleapis.com/css2?family=Arvo:wght@400;700&family=Open+Sans:wght@400;600;700&display=swap">
<style>
:root{
  --blue:#1b8fd2;
  --blue-dark:#0b6fae;
  --blue-deep:#0a5f99;
  --blue-light:#bfe3f6;
  --green:#6fb52c;
  --green-dark:#4f9a17;
  --ink:#333;
  --text:#555;
  --grey-bg:#f1f1f1;
  --white:#fff;
}
*{margin:0;padding:0;box-sizing:border-box}
html,body{width:905px;height:1200px;overflow:hidden}
body{position:relative;background:var(--white);font-family:"Open Sans",Arial,sans-serif;color:var(--text)}
.abs{position:absolute}
.serif{font-family:"Arvo",Georgia,serif}

/* header */
.header{left:0;top:0;width:905px;height:111px;background:linear-gradient(#fdfdfd,#ececec)}
.logo{left:93px;top:30px;display:flex;align-items:center;gap:10px}
.logo-dot{width:38px;height:38px;border-radius:50%;background:var(--blue)}
.logo-name{font-family:"Arvo",Georgia,serif;font-weight:700;font-size:19px;color:var(--blue-dark)}
.tagline{left:142px;top:82px;font-size:8.5px;color:#666}
.address{left:434px;top:42px;font-family:"Arvo",Georgia,serif;font-size:12px;line-height:18px;color:#666}
.head-divider{left:634px;top:34px;width:1px;height:46px;background:#d4d4d4}
.call{left:660px;top:34px;font-family:"Arvo",Georgia,serif;color:#555;font-size:13px}
.call .num{display:block;color:var(--blue);font-size:18px;margin-top:2px}
.call svg{vertical-align:-2px;margin-right:4px}

/* nav */
.nav{left:0;top:111px;width:905px;height:36px;background:linear-gradient(#34a8e4,#0f7fc2);border-bottom:1px solid #0a6aa5}
.nav-list{left:88px;top:0;height:36px;display:flex;list-style:none}
.nav-list li{height:36px;padding:0 12px;display:flex;align-items:center;color:#fff;font-size:11px;font-weight:600;border-right:1px solid rgba(255,255,255,.2)}
.nav-list li.home{width:41px;justify-content:center;background:#0b6fae}
.btn-book{display:flex;align-items:center;justify-content:center;gap:8px;color:#fff;font-weight:600;font-size:12.5px;background:linear-gradient(#86c93b,var(--green-dark));border:1px solid #478b14;border-radius:2px}
.nav .btn-book{position:absolute;left:653px;top:8px;width:158px;height:28px}

/* hero */
.stage{left:0;top:147px;width:905px;height:357px;background:linear-gradient(#f4f4f4,#e6e6e6)}
.hero{left:87px;top:165px;width:730px;height:259px;background:#fff;overflow:hidden;box-shadow:0 2px 6px rgba(0,0,0,.1)}
.hero-photo{left:0;top:0;width:420px;height:259px;background:linear-gradient(110deg,#e9d2bf 0%,#f1e3d6 40%,#dfe8ee 75%,#fff 100%)}
.hero-title{left:355px;top:44px;font-family:"Arvo",Georgia,serif;font-size:23px;line-height:30px;color:#222}
.hero-title b{color:var(--blue-dark)}
.hero-title .l2{padding-left:40px;display:block}
.hero-copy{left:355px;top:110px;width:330px;font-size:11.5px;line-height:17px;color:#333}
.btn-more{left:540px;top:170px;width:114px;height:28px;font-size:12px}
.pager{left:659px;top:238px;display:flex;gap:2px;background:#fff;padding:4px 6px}
.pager span{width:14px;height:14px;font-size:10px;font-weight:700;text-align:center;line-height:14px;color:#333}
.pager span.on{background:var(--blue);color:#fff}

/* tiles */
.tile-strip{left:87px;top:424px;width:730px;height:126px;background:var(--blue-light);border-radius:0 0 6px 6px}
.tile{top:436px;width:170px;height:101px;background:linear-gradient(120deg,#1b8fd2 0%,#49aee3 45%,#c8d8e2 100%);border:2px solid #fff;box-shadow:0 1px 3px rgba(0,0,0,.25);overflow:hidden}
.tile .label{position:absolute;left:6px;top:16px;color:#fff;font-family:"Arvo",Georgia,serif;font-size:16px;line-height:17px}
.tile .label small{display:block;font-family:"Open Sans",Arial,sans-serif;font-size:9.5px;margin-top:2px}
.tile .mini{position:absolute;left:10px;bottom:7px;padding:1px 6px;font-size:8.5px;font-weight:700;color:#fff;background:var(--green)}
.tile.faq{background:linear-gradient(90deg,#1b8fd2,#7ec7ef)}

/* content */
.intro-title{left:90px;top:580px;width:480px;font-family:"Arvo",Georgia,serif;font-size:17px;line-height:23px;color:#222}
.intro-title b{color:var(--blue-dark)}
.body-copy{left:90px;width:470px;font-size:11.3px;line-height:17.5px;color:#555}
.contact-title{left:90px;top:854px;font-family:"Arvo",Georgia,serif;font-size:19px;color:var(--blue)}
.contact-box{left:89px;top:886px;width:472px;height:79px;border:1px solid #ccc;box-shadow:0 1px 3px rgba(0,0,0,.1);padding:12px 20px;text-align:center;font-size:11.3px;line-height:18px;color:#555}
.link{color:var(--blue-dark);font-weight:700}

/* sidebar */
.side-title{left:614px;font-family:"Arvo",Georgia,serif;font-size:14px;color:var(--blue-dark)}
.services{left:618px;top:612px;list-style:none;font-size:10.3px;color:#444}
.services li{height:22px;line-height:22px}
.services li::before{content:"››";color:var(--green);font-weight:700;margin-right:8px}
.sidebar-book{left:617px;top:812px;width:181px;height:28px}
.doc-photo{left:621px;top:892px;width:81px;height:78px;background:linear-gradient(#d9d2cc,#b8a89a);border:3px solid #fff;box-shadow:0 0 0 1px #ccc}
.doc-copy{left:716px;top:890px;width:92px;font-size:9.5px;line-height:13px;color:#555}
.doc-copy b,.doc-copy .more{color:var(--blue-dark);font-weight:700}
.share{left:619px;top:1000px;display:flex;align-items:center;gap:6px;font-family:"Arvo",Georgia,serif;font-size:14px;color:#999}
.share .dots{font-size:11px;margin-right:8px}
.share i{display:inline-block;width:21px;height:21px;border-radius:3px}

/* footer */
.footer{left:0;top:1074px;width:905px;height:126px;background:var(--blue);border-top:4px solid #0b5f94}
.footer-nav{left:105px;top:1094px;display:flex;list-style:none;font-size:8.5px;color:#fff}
.footer-nav li{padding:0 5px;border-right:1px solid rgba(255,255,255,.5)}
.footer-nav li:first-child{padding-left:0}
.footer-nav li:last-child{border:0}
.copyright{left:718px;top:1094px;font-size:8.5px;color:#fff}
.footer-rule{left:87px;top:1114px;width:730px;height:1px;background:rgba(255,255,255,.3)}
.footer-small{left:87px;top:1134px;width:730px;text-align:center;font-size:8px;line-height:11.5px;color:#e6f3fb}
</style>
</head>
<body>

<header class="abs header">
  <div class="abs logo"><span class="logo-dot"></span><span class="logo-name">Orla Dental Clinic</span></div>
  <div class="abs tagline">Values | Innovation | Professionalism</div>
  <div class="abs address">48 Harbour View Rd., Ste. 12<br>Parramatta, NSW 2150</div>
  <div class="abs head-divider"></div>
  <div class="abs call">
    <svg width="12" height="12" viewBox="0 0 12 12"><path d="M3 1l2 3-1.5 1.2a7 7 0 003.3 3.3L8 7l3 2-1 2C5 11 1 7 1 2z" fill="#1b8fd2"/></svg>Call for appointment
    <span class="num">(02) 9555 0148</span>
  </div>
</header>

<nav class="abs nav">
  <ul class="abs nav-list">
    <li class="home"><svg width="12" height="11" viewBox="0 0 12 11"><path d="M6 0l6 5h-2v6H7V7H5v4H2V5H0z" fill="#fff"/></svg></li>
    <li>ABOUT US</li><li>SERVICES WE OFFER</li><li>PATIENT INFORMATION</li><li>FAQ</li><li>CONTACT US</li>
  </ul>
  <div class="btn-book"><svg width="12" height="12" viewBox="0 0 12 12"><rect x="1" y="2" width="10" height="9" fill="#fff"/><rect x="1" y="2" width="10" height="3" fill="#d33"/></svg>Book an Appintment</div>
</nav>

<div class="abs stage"></div>
<section class="abs hero">
  <div class="abs hero-photo" role="img" aria-label="Photo of a smiling young woman in a dental chair"></div>
  <h1 class="abs hero-title"><b>Advanced General</b><span class="l2">&amp; <b>Cosmetic</b> Dentistry</span></h1>
  <p class="abs hero-copy">With Six Month Align® Braces, you could have straight teeth before your next dental cleaning – and most people won't even notice you're wearing braces!</p>
  <div class="abs btn-book btn-more">Learn More ····›</div>
  <div class="abs pager"><span class="on">1</span><span>2</span><span>3</span><span>4</span></div>
</section>

<div class="abs tile-strip"></div>
<div class="abs tile" style="left:102px" role="img" aria-label="Photo of a smiling family of three generations"><span class="label">PATIENTS<br>OF ALL<br>AGES</span><span class="mini">Learn more ››</span></div>
<div class="abs tile" style="left:281px" role="img" aria-label="Photo of the clinic team"><span class="label">OUR<br>TEAM</span><span class="mini">Learn more ››</span></div>
<div class="abs tile" style="left:459px" role="img" aria-label="Photo of a smiling woman"><span class="label" style="font-size:13px">GALLERY<small>View Our Gallry</small></span><span class="mini">Learn more ››</span></div>
<div class="abs tile faq" style="left:637px" role="img" aria-label="Large question mark graphic"><span class="label">FAQ</span><span class="mini">Learn more ››</span></div>

<main>
  <h2 class="abs intro-title"><b>Dentist</b> of <b>NSW</b> first in nswdc to perform Custom lorem ipsum is sumply a dummy text</h2>
  <p class="abs body-copy" style="top:637px">Dr. Anika Rao and his staff are dedicated to provide the state of the art gynecologic and female urology services in Northern New Jersey. We use the latest advances in medicine to care for our patients. We are constantly training and studying to make sure our patients have the latest options available to them. Our office is equipped with the latest diagnostic modalities including ultrasound, urodynamics, colposcopy and hysteroscopy. We offer many in office treatments as well as outpatient surgery options. We always try to get patients into the office as soon as possible with urgent problems.</p>
  <p class="abs body-copy" style="top:776px">Dr. Rao and his staff are proud to provide outstanding gynecology and gynecologic urologic care to women of all ages in Bergen and Passaic Counties of New Jersey.</p>
  <h2 class="abs contact-title">Contact Us Today... (02) 9555 0148</h2>
  <div class="abs contact-box">Our dental office is equipped with leading-edge dental technology,<br>a skilled and compassionate staff, and state-of-the-art patient amenities to make each visit as relaxing and stress-free as possible.</div>
  <p class="abs body-copy" style="top:979px">To get step-by-step directions from your location to our office, click on the roamchart logo in the map above to go to <span class="link">roamchart.</span> You can also read and leave reviews on our roamchart listing.</p>
</main>

<aside>
  <h3 class="abs side-title" style="top:584px">Our Services</h3>
  <ul class="abs services">
    <li>Patients of All Ages</li><li>New Technologies for Comfortable</li><li>Dentistry</li><li>We're Close to Home</li><li>Easy Payment Plans For Everyone</li><li>Professional Teeth Whitening</li><li>Dental Implant Restorations</li><li>Six Month Align® Braces</li>
  </ul>
  <div class="abs btn-book sidebar-book"><svg width="12" height="12" viewBox="0 0 12 12"><rect x="1" y="2" width="10" height="9" fill="#fff"/><rect x="1" y="2" width="10" height="3" fill="#d33"/></svg>Book an Appintment</div>
  <h3 class="abs side-title" style="top:867px">Meet the Doctor</h3>
  <div class="abs doc-photo" role="img" aria-label="Portrait photo of the doctor"></div>
  <p class="abs doc-copy"><b>Dr. Anika</b> Rao practices in Riverbend University Medical Center and at Linden General Hospital, India where he takes...<br><span class="more">read more ····›</span></p>
  <div class="abs share">Share <span class="dots">····›</span>
    <i style="background:#3fb0e8" aria-label="quillpost"></i><i style="background:#3b5b9a" aria-label="chatterbox"></i><i style="background:#1d78b3" aria-label="linkpro"></i><i style="background:#444" aria-label="circlecast"></i>
  </div>
</aside>

<footer class="abs footer"></footer>
<ul class="abs footer-nav"><li>HOME</li><li>ABOUT US</li><li>SERVICES WE OFFER</li><li>PATIENT INFORMATION</li><li>FAQ</li><li>CONTACT US</li></ul>
<div class="abs copyright">© 2011 Orla Dental Clinic</div>
<div class="abs footer-rule"></div>
<p class="abs footer-small">Orla Dental Clinic Associates 21 Elm Street, Suite 4 Parramatta, NSW 2150 Phone (02) 9555 0148 Fax (02) 9555 0149<br>Privacy Policy | Sitemap | Medical Website Design<br>Dr. Owen Marsh specializes in the surgical treatment of cancer and all aspects of general surgery.</p>

</body>
</html>
```